Film and TV production company

I have the logo already designed by mark quarry. I just need the text and the logo attached to the business card. Maybe a small design on the back of the card or text.

Industry/Entity Type

film tv arts

Contact Information for Business Card

Dale Morrow Cinematographer-Director

Colors
F0912C
F2A743
F7CA91
FBE8D2
FDF5EE
EE7325
F08F49
F5BC92
FAE3D3
FDF4ED

Requirements
Must have
• www.copperlanepix.com.au my email address mail@copperlanepix.com.au my mobile number 0491570158
Nice to have
• Some kind of small art work on the back that ties in with the logo design attached
Should not have
• Must clean and simple

```html
<!DOCTYPE html>
<html lang="en">
<head>
<meta charset="utf-8">
<title>Copper Lane Pix – Business Card</title>
<link rel="stylesheet" href="https://fonts.googleapis.com/css2?family=Lato:wght@400;700&display=swap">
<style>
  :root {
    --stage: #3a3a3a;
    --card-dark: #1e1e1e;
    --card-light: #ffffff;
    --foil: #d9d9d9;
    --ink: #1a1a1a;
    --muted: #6b6b6b;
    --copper: #ee7325;
    --divider: #cfcfcf;
  }
  * { margin: 0; padding: 0; box-sizing: border-box; }
  html, body { width: 1200px; height: 689px; overflow: hidden; }
  body {
    background: var(--stage);
    font-family: "Lato", sans-serif;
    position: relative;
  }
  .card {
    position: absolute;
    top: 194px;
    width: 525px;
    height: 300px;
  }
  .card--back { left: 45px; background: var(--card-dark); }
  .card--front { left: 630px; background: var(--card-light); }

  /* Back */
  .back-name {
    position: absolute;
    left: 0; right: 0; top: 50%;
    transform: translateY(-50%);
    text-align: center;
    white-space: nowrap;
    color: var(--foil);
    font-weight: 400;
    font-size: 24px;
    letter-spacing: 0.04em;
  }

  /* Front */
  .brand {
    position: absolute;
    left: 0; right: 0; top: 96px;
    display: flex;
    justify-content: center;
    align-items: center;
    gap: 12px;
    white-space: nowrap;
  }
  .brand__square {
    width: 14px; height: 14px;
    background: var(--ink);
  }
  .brand__name {
    color: var(--ink);
    font-weight: 400;
    font-size: 26px;
    letter-spacing: 0.02em;
  }
  .details {
    position: absolute;
    left: 48px; right: 40px; bottom: 44px;
    display: flex;
    align-items: center;
  }
  .person { flex: 0 0 auto; padding-right: 22px; white-space: nowrap; }
  .person__name {
    color: var(--ink);
    font-weight: 400;
    font-size: 24px;
    letter-spacing: 0.02em;
    text-transform: uppercase;
    line-height: 1.1;
  }
  .person__role {
    color: var(--copper);
    font-size: 14px;
    margin-top: 3px;
  }
  .details__divider {
    width: 1px; height: 62px;
    background: var(--divider);
  }
  .contact {
    list-style: none;
    padding-left: 18px;
    display: flex;
    flex-direction: column;
    gap: 4px;
  }
  .contact__item {
    display: flex;
    align-items: center;
    gap: 9px;
    color: var(--muted);
    font-size: 13px;
    white-space: nowrap;
  }
  .contact__icon { width: 12px; height: 12px; flex: 0 0 auto; }
</style>
</head>
<body>
  <section class="card card--back" aria-label="Card back">
    <p class="back-name">Copper Lane Pix</p>
  </section>

  <section class="card card--front" aria-label="Card front">
    <div class="brand">
      <span class="brand__square"></span>
      <span class="brand__name">Copper Lane Pix</span>
    </div>
    <div class="details">
      <div class="person">
        <p class="person__name">Dale Morrow</p>
        <p class="person__role">Cinematographer-Director</p>
      </div>
      <span class="details__divider"></span>
      <ul class="contact">
        <li class="contact__item">
          <svg class="contact__icon" viewBox="0 0 12 12" aria-hidden="true"><rect x="3" y="0.8" width="6" height="10.4" rx="1.2" fill="none" stroke="#ee7325" stroke-width="1.2"/><circle cx="6" cy="9.3" r="0.7" fill="#ee7325"/></svg>
          0491570158
        </li>
        <li class="contact__item">
          <svg class="contact__icon" viewBox="0 0 12 12" aria-hidden="true"><rect x="0.5" y="2.5" width="11" height="7.5" fill="#ee7325"/><path d="M0.5 2.5 L6 7 L11.5 2.5" fill="none" stroke="#fff" stroke-width="1"/></svg>
          mail@copperlanepix.com.au
        </li>
        <li class="contact__item">
          <svg class="contact__icon" viewBox="0 0 12 12" aria-hidden="true"><circle cx="6" cy="6" r="5.2" fill="#ee7325"/><path d="M0.8 6 H11.2 M6 0.8 C3.5 3.5 3.5 8.5 6 11.2 M6 0.8 C8.5 3.5 8.5 8.5 6 11.2" fill="none" stroke="#fff" stroke-width="0.8"/></svg>
          www.copperlanepix.com.au
        </li>
      </ul>
    </div>
  </section>
</body>
</html>
```